New Australian Beverage Company Needs a Bottle Label Design

We are after a bottle label design for our new aloe vera drinks called 'Sun Ridge'.

There are 5+ different colourrs we would like to compliment the flavors.

We are after a logo that is simple and eye catching.
Updates

Project Deadline Extended Reason: Business partner is currently overseas and would like to review all designs with him upon his return. Added Thursday, May 14, 2015

Project Deadline Extended Reason: We have received a number of great designs and we require more time to decide which direction we would like to take our label design. Thank you for your understanding. Added Thursday, May 21, 2015

Target Market(s)

Our target market is open for all as we would like to supply our drinks to quench everyone's thirst, however our biggest customers would be the teenagers to adults up to around the age of 50.

Industry/Entity Type

It Company

Requirements
Must have
• We are after a refreshing label that catches the eyes and makes you feel like picking it up and drinking it.

```html
<!DOCTYPE html>
<html lang="en">
<head>
<meta charset="utf-8">
<title>Sun Ridge – Aloe Vera Natural Juice Labels</title>
<link href="https://fonts.googleapis.com/css2?family=Oswald:wght@600&family=Courier+Prime:wght@700&family=Roboto+Condensed:wght@400&display=swap" rel="stylesheet">
<style>
  :root {
    --page: #ffffff;
    --cap: #eef0f0;
    --cap-edge: #cfd6d6;
    --mango: #f6b51b;
    --mango-dark: #e99a10;
    --mint: #3f7a2e;
    --mint-dark: #2f6222;
    --berry: #d92a5a;
    --berry-dark: #c01f4b;
    --white: #ffffff;
    --flavour-mango: #e0389a;
    --flavour-mint: #9fd43a;
    --flavour-berry: #f7a8c8;
  }
  * { box-sizing: border-box; margin: 0; padding: 0; }
  html, body { width: 900px; height: 1200px; overflow: hidden; background: var(--page); }
  .range {
    position: relative;
    width: 900px; height: 1200px;
  }
  .bottle {
    position: absolute;
    top: 168px;
    width: 236px;
    height: 880px;
  }
  .bottle--mango { left: 58px; }
  .bottle--mint  { left: 320px; }
  .bottle--berry { left: 612px; }

  .bottle__cap {
    position: absolute;
    left: 40px; top: 0;
    width: 156px; height: 62px;
    background: var(--cap);
    border: 2px solid var(--cap-edge);
    border-radius: 10px 10px 6px 6px;
  }
  .bottle__neck {
    position: absolute;
    left: 50px; top: 60px;
    width: 136px; height: 22px;
    border-radius: 4px;
  }
  .bottle__body {
    position: absolute;
    left: 0; top: 78px;
    width: 236px; height: 802px;
    border-radius: 70px 70px 30px 30px;
    display: flex;
    flex-direction: column;
    align-items: center;
    text-align: center;
    color: var(--white);
  }
  .bottle--mango .bottle__neck,
  .bottle--mango .bottle__body { background: linear-gradient(90deg, var(--mango-dark), var(--mango) 30%, var(--mango) 75%, var(--mango-dark)); }
  .bottle--mint .bottle__neck,
  .bottle--mint .bottle__body { background: linear-gradient(90deg, var(--mint-dark), var(--mint) 30%, var(--mint) 75%, var(--mint-dark)); }
  .bottle--berry .bottle__neck,
  .bottle--berry .bottle__body { background: linear-gradient(90deg, var(--berry-dark), var(--berry) 30%, var(--berry) 75%, var(--berry-dark)); }

  .label__mark {
    margin-top: 300px;
    width: 26px; height: 26px;
    border-radius: 50%;
    background: var(--white);
  }
  .label__brand {
    margin-top: 20px;
    font-family: "Oswald", sans-serif;
    font-weight: 600;
    font-size: 56px;
    line-height: 0.95;
    letter-spacing: 1px;
    color: var(--white);
  }
  .label__tagline {
    margin-top: 10px;
    font-family: "Roboto Condensed", sans-serif;
    font-size: 13px;
    letter-spacing: 0.5px;
    color: var(--white);
  }
  .label__flavour {
    margin-top: 10px;
    font-family: "Courier Prime", monospace;
    font-weight: 700;
    font-size: 24px;
    line-height: 1.1;
    text-transform: uppercase;
  }
  .bottle--mango .label__flavour { color: var(--flavour-mango); }
  .bottle--mint  .label__flavour { color: var(--flavour-mint); }
  .bottle--berry .label__flavour { color: var(--flavour-berry); }
  .label__volume {
    position: absolute;
    top: 824px;
    left: 0; right: 0;
    font-family: "Roboto Condensed", sans-serif;
    font-size: 15px;
    color: var(--white);
  }
  .bottle__body .label__volume { top: 742px; }
</style>
</head>
<body>
<main class="range">
  <article class="bottle bottle--mango">
    <div class="bottle__cap"></div>
    <div class="bottle__neck"></div>
    <div class="bottle__body">
      <span class="label__mark"></span>
      <h2 class="label__brand">SUN<br>RIDGE</h2>
      <p class="label__tagline">ALOE VERA NATURAL JUICE</p>
      <p class="label__flavour">Orange Mango<br>Apricot</p>
      <p class="label__volume">16.9 FL OZ (500 ml)</p>
    </div>
  </article>

  <article class="bottle bottle--mint">
    <div class="bottle__cap"></div>
    <div class="bottle__neck"></div>
    <div class="bottle__body">
      <span class="label__mark"></span>
      <h2 class="label__brand">SUN<br>RIDGE</h2>
      <p class="label__tagline">ALOE VERA NATURAL JUICE</p>
      <p class="label__flavour">Mint Chia</p>
      <p class="label__volume">16.9 FL OZ (500 ml)</p>
    </div>
  </article>

  <article class="bottle bottle--berry">
    <div class="bottle__cap"></div>
    <div class="bottle__neck"></div>
    <div class="bottle__body">
      <span class="label__mark"></span>
      <h2 class="label__brand">SUN<br>RIDGE</h2>
      <p class="label__tagline">ALOE VERA NATURAL JUICE</p>
      <p class="label__flavour">Strawberry<br>Cranberry</p>
      <p class="label__volume">16.9 FL OZ (500 ml)</p>
    </div>
  </article>
</main>
</body>
</html>
```